wedding package brochure

We want to freshen the look for our wedding packages. Attached is a link to the current content
http://www.tarwinheadslinks.com.au/weddings/THL-Wedding-Package-2012-2013.pdf
We would like the logo (the dolphins) included and it needs to showcase the beachside location and give a classy wedding feel. I have a style guide available if required.

Industry/Entity Type

Wedding

```html
<!DOCTYPE html>
<html lang="en">
<head>
<meta charset="utf-8">
<title>Tarwin Heads Links – Wedding Package</title>
<link href="https://fonts.googleapis.com/css2?family=Oswald:wght@600&family=Roboto+Condensed:wght@400;700&display=swap" rel="stylesheet">
<style>
  :root{
    --red:#e0201f;
    --ink:#4d4d4f;
    --panel:#29292b;
    --white:#ffffff;
    --frame:#6e6e70;
    --tick:#9a9a9a;
    --label:#333333;
  }
  *{margin:0;padding:0;box-sizing:border-box}
  html,body{width:1200px;height:423px;overflow:hidden;background:var(--white)}
  .spread{position:relative;width:1200px;height:423px;font-family:"Roboto Condensed",Arial,sans-serif}
  .page-number{position:absolute;top:9px;font-size:15px;color:var(--label)}
  .page-number--left{left:34px}
  .page-number--right{left:1141px}
  .brand{position:absolute;top:14px;font-size:6.5px;font-weight:700;color:var(--red);white-space:nowrap}
  .brand--left{left:68px}
  .brand--right{left:1053px}
  .rule{position:absolute;top:13px;left:142px;width:904px;height:9px;
    background:repeating-linear-gradient(90deg,var(--tick) 0 1px,transparent 1px 3px)}
  .title{position:absolute;left:28px;top:64px;font-family:"Oswald",Impact,sans-serif;font-weight:600;font-size:19px;line-height:24px;color:var(--red)}
  .intro p{position:absolute;left:28px;width:430px;font-size:10.4px;line-height:14.5px;letter-spacing:-0.05px;color:var(--ink)}
  .photo{position:absolute;left:472px;width:92px;height:97px;border:4px solid var(--frame);border-radius:6px}
  .photo--terrace{top:65px;background:linear-gradient(180deg,#3a5fa8,#8a8f9a)}
  .photo--beach{top:175px;background:linear-gradient(180deg,#6cc0e6,#e6dcc4)}
  .photo--sunset{top:285px;background:linear-gradient(180deg,#f2dcc6,#c99474)}
  .panel{position:absolute;left:596px;top:62px;width:566px;height:318px;background:var(--panel);border-radius:0 26px 26px 0}
  .panel ul{list-style:none}
  .panel li{position:absolute;left:29px;width:510px;font-size:10.4px;line-height:14.5px;letter-spacing:-0.05px;color:var(--white)}
  .panel li::before{content:"";position:absolute;left:-16px;top:3px;width:8px;height:8px;background:var(--red)}
</style>
</head>
<body>
<div class="spread">
  <span class="page-number page-number--left">01</span>
  <span class="brand brand--left">TARWIN HEADS LINKS</span>
  <div class="rule"></div>
  <span class="brand brand--right">TARWIN HEADS LINKS</span>
  <span class="page-number page-number--right">02</span>

  <h1 class="title">About our venue</h1>
  <div class="intro">
    <p style="top:101px">Tarwin Heads Links has two venues to choose from for your upcoming wedding, either the spectacular views of Tarwin Heads Beach or the picturesque surrounds of Ridgeview Golf Course. At Tarwin Heads Beachside Golf Club we offer a private room &amp; adjacent terrace with majestic views of Tarwin Heads Beach. At Ridgeview Golf Club we offer picturesque views overlooking the 18 hole championship golf course.</p>
    <p style="top:207px">Tarwin Heads is only two and half hours' drive from Sydney and Canberra making it the perfect wedding destination. A wonderful venue for your wedding celebration, The Beachside or Ridgeview Club House has all the facilities to ensure that your day is a success.</p>
    <p style="top:283px">The room at Beachside is filled with natural light, offering spectacular views of the beach &amp; seating up to 200 guests (varies with floor plans): the adjoining Outdoor Terrace is ideally suited for Pre-dinner drinks or a more casual area for guests to relax.</p>
  </div>

  <div class="photo photo--terrace" role="img" aria-label="Photo of the outdoor terrace"></div>
  <div class="photo photo--beach" role="img" aria-label="Photo of the beach"></div>
  <div class="photo photo--sunset" role="img" aria-label="Photo of the beach at sunset"></div>

  <section class="panel">
    <ul>
      <li style="top:28px">Ridgeview offers a more serene atmosphere, nestled amongst beautiful gardens, having superb views across the picturesque 18 hole championship golf course to the sparkling waters of the Pacific Ocean. Comfortably seating 100 guests the Ridgeview is yours for the evening. The privacy of having the clubhouse to yourself &amp; ample room for parking space are just a couple of factors that make Ridgeview the perfect choice for your wedding.</li>
      <li style="top:118px">Attention to detail &amp; intuitive friendly service makes Tarwin Heads Links the perfect location for your upcoming wedding, the experienced staff will be more than happy to cater for your every need.</li>
      <li style="top:179px">Our Wedding package includes canapés on arrival for your guests, a quality menu selection with a five hour beverage package &amp; a magnificent room overlooking Tarwin Heads Beach or Ridgeview gardens.</li>
      <li style="top:242px">After reading our wedding prospectus, the conference and events team would welcome the opportunity to answer any questions you may have.</li>
    </ul>
  </section>
</div>
</body>
</html>
```